Morvex Business Card (intended for Business Card sized magnet)

Hi guys,

I would like to get a design for my business card for the restaurant. The design must be single sided as I intend to produce business card sized magnets.

The File attached must me on and I'm open for new ides

Can you please ensure that the design meets Cardowell's magnetic business card size specifications:

http://www.cardowell.example.au/custom-magnets.aspx?txi=15695&xnid=TopNav_Magnetic+Business+Cards+(linked+item)_Magnets_Marketing+Products&xnav=TopNav

Full Bleed Size (starting document size):
90 x 52 mm
1062 x 615 pixels
* Finished artwork should use the full bleed dimensions for best results.

Document Trim Size (final size after being cut):
87 x 49 mm
1028 x 579 pixels
* Please be sure to keep all text within the safe margin.

Resolution:
300 DPI

The winning design/source files need to meet these specifications.

Thanks
Updates

Hi guys, can I see more options please Thanks

```html
<!DOCTYPE html>
<html lang="en">
<head>
<meta charset="utf-8">
<title>Morvex Business Card</title>
<link rel="stylesheet" href="https://fonts.googleapis.com/css2?family=Josefin+Sans:wght@300&family=Open+Sans:wght@400&display=swap">
<style>
  :root {
    --teal: #00acc4;
    --teal-dark: #1b6b86;
    --ink: #222222;
    --text-grey: #555555;
    --frame: #444444;
    --paper: #ffffff;
    --pattern-tone: linear-gradient(90deg, #d9d9d9, #bfbfbf 30%, #e6e6e6 50%, #bfbfbf 70%, #d9d9d9);
  }
  html, body {
    margin: 0;
    padding: 0;
    width: 1200px;
    height: 1002px;
    overflow: hidden;
    background: var(--paper);
  }
  .board {
    position: relative;
    width: 1200px;
    height: 1002px;
  }
  .board-frame {
    position: absolute;
    left: 1px;
    top: 3px;
    width: 1197px;
    height: 997px;
    border: 2px solid var(--frame);
    box-sizing: border-box;
  }
  .corner-pattern {
    position: absolute;
    width: 142px;
    height: 44px;
    background: var(--pattern-tone);
    border-top: 2px solid var(--ink);
    border-bottom: 2px solid var(--ink);
  }
  .corner-pattern--top { left: 1058px; top: 8px; }
  .corner-pattern--bottom { left: 2px; top: 952px; }

  .card {
    position: absolute;
    width: 469px;
    height: 264px;
    background: var(--paper);
    outline: 1px solid var(--frame);
    overflow: hidden;
    font-family: "Open Sans", sans-serif;
  }
  .card--flat { left: 378px; top: 206px; }
  .card--tilted {
    left: 590px;
    top: 464px;
    transform-origin: 0 0;
    transform: rotate(20.8deg);
  }
  .card-band {
    position: absolute;
    left: 0;
    top: 0;
    width: 469px;
    height: 264px;
  }
  .brand-name {
    position: absolute;
    left: 6px;
    top: 78px;
    width: 143px;
    text-align: center;
    font-family: "Josefin Sans", sans-serif;
    font-weight: 300;
    font-size: 38px;
    line-height: 1;
    color: var(--ink);
    white-space: nowrap;
  }
  .brand-pattern {
    position: absolute;
    left: 6px;
    top: 129px;
    width: 143px;
    height: 42px;
    background: var(--pattern-tone);
    border-top: 2px solid var(--ink);
    border-bottom: 2px solid var(--ink);
  }
  .holder-name {
    position: absolute;
    left: 286px;
    top: 30px;
    font-family: "Josefin Sans", sans-serif;
    font-weight: 300;
    font-size: 36px;
    line-height: 1;
    color: var(--teal-dark);
    white-space: nowrap;
  }
  .holder-role {
    position: absolute;
    left: 290px;
    top: 68px;
    font-family: "Josefin Sans", sans-serif;
    font-weight: 300;
    font-size: 20px;
    line-height: 1;
    color: var(--teal-dark);
  }
  .contact-list {
    position: absolute;
    left: 264px;
    top: 127px;
    margin: 0;
    padding: 0;
    list-style: none;
  }
  .contact-item {
    position: relative;
    padding-left: 32px;
    font-size: 13.5px;
    line-height: 20px;
    color: var(--text-grey);
    white-space: nowrap;
  }
  .contact-item--phone { margin-bottom: 6px; }
  .contact-item--email { margin-bottom: 10px; }
  .contact-item--address { margin-bottom: 6px; }
  .contact-item--web { font-size: 15px; }
  .contact-icon {
    position: absolute;
    left: 0;
    top: 3px;
    width: 14px;
    height: 14px;
  }
</style>
</head>
<body>
<main class="board">
  <div class="board-frame"></div>
  <div class="corner-pattern corner-pattern--top" role="img" aria-label="Decorative geometric star border with red, teal and yellow accents"></div>
  <div class="corner-pattern corner-pattern--bottom" role="img" aria-label="Decorative geometric star border with red, teal and yellow accents"></div>

  <article class="card card--flat">
    <svg class="card-band" viewBox="0 0 469 264" aria-hidden="true">
      <path d="M153 0 H182 V100 C184 170 200 215 257 264 H155 Z" fill="var(--teal)"/>
    </svg>
    <div class="brand-name">Morvex</div>
    <div class="brand-pattern" role="img" aria-label="Decorative geometric star border with red, teal and yellow accents"></div>
    <div class="holder-name">Morvex</div>
    <div class="holder-role">owner</div>
    <ul class="contact-list">
      <li class="contact-item contact-item--phone">
        <svg class="contact-icon" viewBox="0 0 14 14" aria-hidden="true"><path d="M3 1 L5 1 L6 4 L4.5 5.2 C5.3 7 6.8 8.6 8.6 9.5 L9.8 8 L13 9 L13 11 C13 12 12 13 11 13 C6 12.5 1.5 8 1 3 C1 2 2 1 3 1 Z" fill="var(--teal)"/></svg>
        03 9000 4127
      </li>
      <li class="contact-item contact-item--email">
        <svg class="contact-icon" viewBox="0 0 14 14" aria-hidden="true"><rect x="1" y="3" width="12" height="8" fill="none" stroke="var(--teal)" stroke-width="1"/><path d="M1 3 L7 8 L13 3" fill="none" stroke="var(--teal)" stroke-width="1"/></svg>
        morvex678@morvex.au
      </li>
      <li class="contact-item contact-item--address">
        <svg class="contact-icon" viewBox="0 0 14 14" aria-hidden="true"><path d="M7 0.5 C4.2 0.5 2.5 2.5 2.5 5 C2.5 8 7 13.5 7 13.5 C7 13.5 11.5 8 11.5 5 C11.5 2.5 9.8 0.5 7 0.5 Z M7 3.2 A1.8 1.8 0 1 1 7 6.8 A1.8 1.8 0 1 1 7 3.2 Z" fill="var(--teal)" fill-rule="evenodd"/></svg>
        412 Harlow st,<br>brenton east, 3190
      </li>
      <li class="contact-item contact-item--web">
        <svg class="contact-icon" viewBox="0 0 14 14" aria-hidden="true"><circle cx="7" cy="7" r="5" fill="none" stroke="var(--teal)" stroke-width="1"/><ellipse cx="7" cy="7" rx="2.2" ry="5" fill="none" stroke="var(--teal)" stroke-width="0.8"/><path d="M2 7 H12 M3 4.5 H11 M3 9.5 H11" stroke="var(--teal)" stroke-width="0.8"/></svg>
        www.morvex.com.au
      </li>
    </ul>
  </article>

  <article class="card card--tilted">
    <svg class="card-band" viewBox="0 0 469 264" aria-hidden="true">
      <path d="M153 0 H182 V100 C184 170 200 215 257 264 H155 Z" fill="var(--teal)"/>
    </svg>
    <div class="brand-name">Morvex</div>
    <div class="brand-pattern" role="img" aria-label="Decorative geometric star border with red, teal and yellow accents"></div>
    <div class="holder-name">Morvex</div>
    <div class="holder-role">owner</div>
    <ul class="contact-list">
      <li class="contact-item contact-item--phone">
        <svg class="contact-icon" viewBox="0 0 14 14" aria-hidden="true"><path d="M3 1 L5 1 L6 4 L4.5 5.2 C5.3 7 6.8 8.6 8.6 9.5 L9.8 8 L13 9 L13 11 C13 12 12 13 11 13 C6 12.5 1.5 8 1 3 C1 2 2 1 3 1 Z" fill="var(--teal)"/></svg>
        03 9000 4127
      </li>
      <li class="contact-item contact-item--email">
        <svg class="contact-icon" viewBox="0 0 14 14" aria-hidden="true"><rect x="1" y="3" width="12" height="8" fill="none" stroke="var(--teal)" stroke-width="1"/><path d="M1 3 L7 8 L13 3" fill="none" stroke="var(--teal)" stroke-width="1"/></svg>
        morvex678@morvex.au
      </li>
      <li class="contact-item contact-item--address">
        <svg class="contact-icon" viewBox="0 0 14 14" aria-hidden="true"><path d="M7 0.5 C4.2 0.5 2.5 2.5 2.5 5 C2.5 8 7 13.5 7 13.5 C7 13.5 11.5 8 11.5 5 C11.5 2.5 9.8 0.5 7 0.5 Z M7 3.2 A1.8 1.8 0 1 1 7 6.8 A1.8 1.8 0 1 1 7 3.2 Z" fill="var(--teal)" fill-rule="evenodd"/></svg>
        412 Harlow st,<br>brenton east, 3190
      </li>
      <li class="contact-item contact-item--web">
        <svg class="contact-icon" viewBox="0 0 14 14" aria-hidden="true"><circle cx="7" cy="7" r="5" fill="none" stroke="var(--teal)" stroke-width="1"/><ellipse cx="7" cy="7" rx="2.2" ry="5" fill="none" stroke="var(--teal)" stroke-width="0.8"/><path d="M2 7 H12 M3 4.5 H11 M3 9.5 H11" stroke="var(--teal)" stroke-width="0.8"/></svg>
        www.morvex.com.au
      </li>
    </ul>
  </article>
</main>
</body>
</html>
```